VOSKE - New website for high-quality knives, aprons, chopping boards and caps for Grillers

We would like to develop a new website for our brand-new outdoor cooking brand VOSKE. VOSKE is a brand by grillers for grillers. Therefore the griller will always be in the centre of everything that we do. We want to appear as a cool, robust brand without being too stereotypical (like any other BBQ brands (so not too much black, red, flames)). We're very international and that should also come back in the design.

Main colour will be the yellow supported by red white and black. However, we're also open to other colours

VOSKE will be sold in-store but we want to provide more information to our clients via the website. This will be done through detailed descriptions but also blogs and downloads. We will work together with influencers to share recipes in our Pavane (magazine) and on our blog page.

Website needs to be responsive (web+mobile) and our own team should be able to easily add new content to the website.

Target Market(s)

International grillers or home chefs

Industry/Entity Type

BBQ and outdoor cooking

Coding

Coded - Design and coding required

Other font styles liked:
• Allan & Cambria

Colors

Designer to choose colors to be used in the design.

Requirements
Must have
• home, products (not shop), blog, contact, socials, downloads (for Pavane).
Nice to have
• instagram grid with #voske
Should not have
• too stereotypical BBQ website (red, flames, black)

```html
<!DOCTYPE html>
<html lang="nl">
<head>
<meta charset="utf-8">
<title>VOSKE – Blog</title>
<link href="https://fonts.googleapis.com/css2?family=Poppins:wght@600;700;800;900&display=swap" rel="stylesheet">
<style>
  :root {
    --yellow: #f8c51c;
    --black: #0a0a0a;
    --white: #ffffff;
  }
  * { margin: 0; padding: 0; box-sizing: border-box; }
  html, body { width: 1200px; height: 750px; overflow: hidden; background: var(--white); }
  body { font-family: 'Poppins', sans-serif; color: var(--black); position: relative; }

  .side-tile { position: absolute; left: 0; width: 291px; }
  .side-tile--top {
    top: 0; height: 274px;
    background:
      radial-gradient(ellipse 60% 45% at 35% 30%, rgba(190,190,190,0.55), transparent 70%),
      radial-gradient(ellipse 50% 40% at 80% 25%, rgba(120,120,120,0.5), transparent 70%),
      linear-gradient(170deg, #4a4a4a 0%, #262626 55%, #121212 100%);
  }
  .side-tile--bottom {
    top: 476px; height: 274px;
    background:
      radial-gradient(ellipse 45% 35% at 30% 20%, rgba(200,200,200,0.55), transparent 70%),
      radial-gradient(ellipse 40% 40% at 75% 45%, rgba(140,140,140,0.45), transparent 70%),
      linear-gradient(200deg, #3e3e3e 0%, #1c1c1c 60%, #0e0e0e 100%);
  }
  .side-tile__label {
    position: absolute; left: 0; right: 0; text-align: center;
    color: var(--white); font-weight: 700; font-size: 18.5px; line-height: 24px;
    text-shadow: 0 1px 3px rgba(0,0,0,0.4);
  }
  .side-tile__bar { position: absolute; left: 130px; width: 21px; height: 3px; background: var(--yellow); }
  .side-tile--top .side-tile__label { top: 139px; }
  .side-tile--top .side-tile__bar { top: 172px; }
  .side-tile--bottom .side-tile__label { top: 125px; }
  .side-tile--bottom .side-tile__bar { top: 158px; }

  .page-title {
    position: absolute; left: 35px; top: 328px;
    font-size: 78px; font-weight: 900; letter-spacing: 1px; line-height: 1;
  }

  .brand {
    position: absolute; left: 323px; top: 21px; height: 116px;
    display: flex; align-items: center; gap: 10px;
  }
  .brand__dot { width: 30px; height: 30px; border-radius: 50%; background: var(--yellow); }
  .brand__name { font-weight: 800; font-size: 30px; color: var(--black); letter-spacing: 0.5px; }

  .main-nav { position: absolute; right: 42px; top: 68px; display: flex; gap: 27px; }
  .main-nav__link {
    font-weight: 800; font-size: 20.5px; color: var(--black); text-decoration: none;
    position: relative; line-height: 30px;
  }
  .main-nav__link--active::after {
    content: ""; position: absolute; left: 0; top: 33px;
    width: 21px; height: 4px; background: var(--yellow);
  }

  .post { position: absolute; width: 260px; }
  .post__photo { width: 260px; }
  .post__title {
    font-weight: 700; font-size: 15px; line-height: 22.5px; margin-top: 14px; max-width: 215px;
  }
  .post__title--highlight { color: var(--yellow); }

  .photo--apron-man {
    height: 325px;
    background:
      radial-gradient(ellipse 35% 25% at 45% 8%, rgba(215,215,215,0.8), transparent 75%),
      radial-gradient(ellipse 35% 55% at 50% 60%, rgba(30,30,30,0.85), transparent 75%),
      radial-gradient(ellipse 40% 30% at 90% 85%, rgba(200,200,200,0.6), transparent 75%),
      linear-gradient(180deg, #8a8a8a 0%, #5e5e5e 40%, #9a9a9a 100%);
  }
  .photo--knife-roll {
    height: 162px;
    background:
      radial-gradient(ellipse 25% 40% at 22% 30%, rgba(210,210,210,0.7), transparent 75%),
      radial-gradient(ellipse 40% 40% at 70% 40%, rgba(160,160,160,0.55), transparent 75%),
      linear-gradient(160deg, #505050 0%, #2a2a2a 60%, #3c3c3c 100%);
  }
  .photo--friends {
    height: 192px;
    background:
      radial-gradient(ellipse 30% 40% at 15% 25%, rgba(188,206,120,0.85), transparent 75%),
      radial-gradient(ellipse 35% 45% at 70% 55%, rgba(70,130,145,0.9), transparent 75%),
      radial-gradient(ellipse 30% 25% at 45% 85%, rgba(220,175,90,0.8), transparent 75%),
      linear-gradient(180deg, #7f8f4e 0%, #5f7f76 55%, #dfe3e8 100%);
  }
  .photo--barrel {
    height: 286px;
    background:
      radial-gradient(ellipse 20% 25% at 55% 25%, rgba(70,70,70,0.8), transparent 75%),
      radial-gradient(ellipse 30% 30% at 50% 80%, rgba(15,15,15,0.95), transparent 75%),
      linear-gradient(180deg, #efefef 0%, #dcdcdc 55%, #bdbdbd 100%);
  }
  .photo--badge {
    height: 255px;
    background:
      radial-gradient(ellipse 22% 20% at 62% 58%, rgba(190,190,190,0.85), transparent 75%),
      radial-gradient(ellipse 25% 45% at 8% 50%, rgba(170,170,170,0.6), transparent 75%),
      linear-gradient(160deg, #5a5a5a 0%, #3c3c3c 55%, #4a4a4a 100%);
  }
  .photo--kamado {
    height: 232px;
    background:
      radial-gradient(ellipse 35% 40% at 30% 30%, rgba(15,15,15,0.95), transparent 75%),
      radial-gradient(ellipse 30% 30% at 85% 20%, rgba(220,220,220,0.75), transparent 75%),
      radial-gradient(ellipse 30% 20% at 55% 95%, rgba(210,210,210,0.7), transparent 75%),
      linear-gradient(160deg, #9a9a9a 0%, #4a4a4a 55%, #7a7a7a 100%);
  }
</style>
</head>
<body>

  <div class="side-tile side-tile--top" role="img" aria-label="Black-and-white photo of hands fastening a leather knife roll beside a cap">
    <span class="side-tile__label">VERKOOPPUNTEN</span>
    <span class="side-tile__bar"></span>
  </div>

  <h1 class="page-title">BLOG</h1>

  <div class="side-tile side-tile--bottom" role="img" aria-label="Black-and-white photo of hands lifting knives from a leather knife roll on a grill">
    <span class="side-tile__label">PRODUCTEN</span>
    <span class="side-tile__bar"></span>
  </div>

  <div class="brand">
    <span class="brand__dot"></span>
    <span class="brand__name">VOSKE</span>
  </div>

  <nav class="main-nav">
    <a class="main-nav__link" href="#">HOME</a>
    <a class="main-nav__link" href="#">PRODUCTS</a>
    <a class="main-nav__link main-nav__link--active" href="#">BLOG</a>
    <a class="main-nav__link" href="#">CONTACT</a>
  </nav>

  <article class="post" style="left:327px; top:158px;">
    <div class="post__photo photo--apron-man" role="img" aria-label="Black-and-white photo of a griller in a leather apron sliding a knife into its holster"></div>
    <h2 class="post__title">Het is al geruime tijd een bekend</h2>
  </article>
  <div class="post photo--knife-roll" style="left:327px; top:588px;" role="img" aria-label="Black-and-white photo of hands buckling a leather knife roll next to a cap"></div>

  <article class="post" style="left:612px; top:158px;">
    <div class="post__photo photo--friends" role="img" aria-label="Colour photo of friends laughing at an outdoor table with drinks and bread"></div>
    <h2 class="post__title post__title--highlight">Lorem Ipsum is slechts een proeftekst</h2>
  </article>
  <div class="post photo--barrel" style="left:612px; top:464px;" role="img" aria-label="Black-and-white photo of a man in cap and apron sharpening a knife over a barrel grill"></div>

  <article class="post" style="left:897px; top:158px;">
    <div class="post__photo photo--badge" role="img" aria-label="Close-up black-and-white photo of a leather apron with a metal badge"></div>
    <h2 class="post__title">In tegenstelling tot wat algemeen</h2>
  </article>
  <div class="post photo--kamado" style="left:897px; top:518px;" role="img" aria-label="Black-and-white photo of gloved hands tending a ceramic kamado grill"></div>

</body>
</html>
```